QTR Business Card

Harborline Capital Partners is a successful and reputable financial services company.Our main services are home loans, commercial loans, vehicle finance and equipment finance. We also do development finance for property developers. Our company is always evolving to always be an industry leader in best financial service practices with access to the largest range of lenders in the country.

We want the business card to reflect our national finance company. Modern, professional corporate image. At the same time the concept of Harborline Capital Partners is that we help build wealth for you but the process for the client is an enjoyable peaceful experience. Not stressful at all .....

Colors to be same as the logo .... gold silver black white as the options

On the reverse side of the card I wanted either just the logo symbol or the logo symbol and text of the logo ....

It could be on a black background ..... or silver or gold .... want it to be quite striking to look at when you first see the card.

On the other side of the card I wanted the following details:

Doran Pelham
Director

0498 372 604

doran@hbcpx.com.au

Po Box 852
Tarrow ACT 2694

www.hbcpx.com.au

ACN 918 264 057 (This can be in very small print and can be in the bottom corner of the card or somewhere not very prominent)
Updates

As requested Ive uploaded the logo file in both .ai and .pdf formats. Please let me know if you need anything else. Thanks

Reason: Still deciding on which design I like best. I will provide individual feedback as well.

```html
<!DOCTYPE html>
<html lang="en">
<head>
<meta charset="utf-8">
<title>QTR Business Card – Harborline Capital Partners</title>
<link rel="stylesheet" href="https://fonts.googleapis.com/css2?family=Cinzel:wght@500&family=Gelasio:wght@400&family=Open+Sans:wght@400&display=swap">
<style>
  :root {
    --gold: #c9a42a;
    --gold-light: #e6c766;
    --silver: #8a9598;
    --ink: #111111;
    --paper: #ffffff;
    --text: #1a1a1a;
  }
  * { margin: 0; padding: 0; box-sizing: border-box; }
  html, body {
    width: 964px; height: 1200px; overflow: hidden;
    background: var(--paper);
  }
  body { position: relative; font-family: "Gelasio", Georgia, serif; color: var(--text); }

  .card {
    position: absolute; left: 76px; width: 819px; height: 513px;
    border: 3px solid var(--ink); background: var(--paper); overflow: hidden;
  }
  .card--front { top: 69px; }
  .card--back { top: 640px; }

  .brand-mark {
    position: absolute; border-radius: 50%;
    border: 6px solid var(--silver); background: var(--paper);
  }
  .card--front .brand-mark { left: 24px; top: 25px; width: 118px; height: 118px; }
  .card--back .brand-mark { left: 290px; top: 52px; width: 236px; height: 236px; }

  .brand-name {
    position: absolute; font-family: "Cinzel", "Times New Roman", serif;
    font-weight: 500; color: var(--gold); line-height: 1.05;
  }
  .card--front .brand-name { left: 160px; top: 42px; font-size: 34px; width: 330px; }
  .card--back .brand-name { left: 0; right: 0; top: 318px; text-align: center; font-size: 46px; }

  .company-number {
    position: absolute; left: 318px; top: 124px;
    font-family: "Open Sans", Arial, sans-serif; font-size: 16px; color: var(--text);
    letter-spacing: 0.5px;
  }

  .ornament {
    position: absolute; left: 708px; top: 0; width: 80px; height: 430px; z-index: 0;
    background: linear-gradient(180deg, #f5ebc8, #efe2b6);
  }

  .name-plate {
    position: absolute; left: 476px; top: 182px; width: 337px; height: 105px; z-index: 2;
    background: var(--ink); color: var(--paper); text-align: center; padding-top: 9px;
  }
  .name-plate .person { font-size: 36px; line-height: 1.2; }
  .name-plate .role { font-size: 29px; line-height: 1.2; }

  .contact {
    position: absolute; left: 18px; top: 342px; font-size: 31px; line-height: 1.3;
  }
  .divider {
    position: absolute; left: 370px; top: 346px; width: 2px; height: 70px; background: var(--ink);
  }
  .address {
    position: absolute; left: 400px; top: 344px; font-size: 29px; line-height: 1.35;
  }

  .web-band {
    position: absolute; left: 0; right: 0; bottom: 0; height: 67px; z-index: 2;
    background: var(--gold); color: var(--paper);
    text-align: center; font-size: 30px; line-height: 64px;
  }
  .card--front .web-band { height: 66px; }
</style>
</head>
<body>
  <section class="card card--front" aria-label="Business card front">
    <div class="brand-mark"></div>
    <div class="brand-name">Harborline Capital Partners</div>
    <div class="company-number">ACN 918 264 057</div>

    <div class="ornament" role="img" aria-label="Decorative gold beaded wave lines"></div>

    <div class="name-plate">
      <div class="person">Doran Pelham</div>
      <div class="role">Director</div>
    </div>

    <div class="contact">
      <div>0498 372 604</div>
      <div>doran@hbcpx.com.au</div>
    </div>
    <div class="divider"></div>
    <div class="address">
      <div>Po Box 852,</div>
      <div>Tarrow ACT 2694.</div>
    </div>

    <div class="web-band">www.hbcpx.com.au</div>
  </section>

  <section class="card card--back" aria-label="Business card back">
    <div class="brand-mark"></div>
    <div class="brand-name">Harborline Capital Partners</div>
    <div class="web-band">www.hbcpx.com.au</div>
  </section>
</body>
</html>
```